Powerpoint Presentation

We have a basic 8 page presentation that we would like created on powerpoint. The presentation is very simple dot points and we would like to jazz it up with relevant photos/images relating to the topic on each page.

The topic of the presentation is 'creating a powerful presence and knowing your personal brand' (see attached files).

Target Market(s)

Business women

Requirements
Must have
• Images that match the content on each page

```html
<!DOCTYPE html>
<html lang="en">
<head>
<meta charset="utf-8">
<title>What is Presence?</title>
<link rel="stylesheet" href="https://fonts.googleapis.com/css2?family=Carlito:ital,wght@0,400;0,700;1,400&display=swap">
<style>
  :root {
    --sky-deep: #0a8bd6;
    --sky-mid: #3fb0ea;
    --sky-light: #9ddaf5;
    --paper: #ffffff;
    --title: #ffffff;
    --ink-navy: #1d3579;
    --card-fill: #f7f2e6;
    --card-edge: #d9c7a0;
    --art-warm: #f1e3c8;
    --art-soft: #faf4e9;
    --brand-orange: #e8542a;
    --brand-grey: #8a8a8a;
  }
  html, body {
    margin: 0;
    padding: 0;
    overflow: hidden;
  }
  .slide {
    position: relative;
    width: 1200px;
    height: 900px;
    background: var(--paper);
    overflow: hidden;
    font-family: "Carlito", "Calibri", sans-serif;
  }
  .slide__header {
    position: absolute;
    inset: 0;
    width: 1200px;
    height: 900px;
  }
  .slide__title {
    position: absolute;
    top: 92px;
    left: 0;
    width: 1200px;
    margin: 0;
    text-align: center;
    color: var(--title);
    font-size: 68px;
    line-height: 80px;
    font-weight: 700;
  }
  .figure-art {
    position: absolute;
    left: 267px;
    top: 342px;
    width: 600px;
    height: 558px;
    background: linear-gradient(180deg, var(--art-soft) 0%, var(--art-warm) 55%, var(--art-soft) 100%);
  }
  .quote-card {
    position: absolute;
    left: 380px;
    top: 537px;
    width: 408px;
    height: 250px;
    box-sizing: border-box;
    padding: 32px 0 0 24px;
    background: var(--card-fill);
    border: 3px solid var(--card-edge);
    border-radius: 4px;
    box-shadow: 0 3px 8px rgba(120, 90, 40, 0.25);
  }
  .quote-card__text {
    margin: 0;
    color: var(--ink-navy);
    font-style: italic;
    font-size: 47px;
    line-height: 42px;
    white-space: nowrap;
  }
  .brand {
    position: absolute;
    left: 16px;
    top: 800px;
  }
  .brand__mark {
    display: block;
    width: 40px;
    height: 40px;
    background: var(--brand-orange);
  }
  .brand__name {
    display: block;
    margin-top: 20px;
    color: var(--brand-grey);
    font-size: 24px;
  }
</style>
</head>
<body>
<main class="slide">
  <svg class="slide__header" viewBox="0 0 1200 900" aria-hidden="true">
    <defs>
      <linearGradient id="sky" x1="0" y1="0" x2="0" y2="1">
        <stop offset="0" stop-color="var(--sky-deep)"/>
        <stop offset="0.6" stop-color="var(--sky-mid)"/>
        <stop offset="1" stop-color="var(--sky-light)"/>
      </linearGradient>
    </defs>
    <path d="M0 0 H1200 V300 C1020 250 900 245 760 275 C600 310 420 230 0 255 Z" fill="url(#sky)"/>
    <path d="M0 255 C300 225 520 250 700 300 C880 350 1050 290 1200 260 V340 C1050 330 900 345 760 330 C560 300 300 230 0 265 Z" fill="var(--paper)"/>
    <path d="M360 232 C620 240 780 300 1200 255" fill="none" stroke="var(--paper)" stroke-width="3" opacity="0.7"/>
    <path d="M700 290 C900 300 1050 270 1200 225" fill="none" stroke="var(--paper)" stroke-width="2" opacity="0.6"/>
    <path d="M760 275 C920 320 1080 320 1200 300 V330 C1060 330 900 330 760 300 Z" fill="var(--sky-light)" opacity="0.5"/>
  </svg>

  <h1 class="slide__title">What is Presence?</h1>

  <div class="figure-art" role="img" aria-label="Illustration of a simple figure holding up a sign"></div>

  <div class="quote-card">
    <p class="quote-card__text">"The state of<br>being present in a<br>&nbsp;situation or with<br>a person"</p>
  </div>

  <div class="brand">
    <span class="brand__mark"></span>
    <span class="brand__name">Fairhaven</span>
  </div>
</main>
</body>
</html>
```